Web Application Graphic Design Project

We need a design for an online literacy application. The target audience are 9-12 year old children and the application will teach them literacy skills, like essay writing. It is a web-based application called Brivolen and the software developers now need a graphic design to implement into the code - no coding required, just design of the layout.
Wireframes are attached to give an overview of what the functionalities are - it runs in any ordinary web-browser (indicated in the wireframes as well). The application consists of a static background (workspace) onto which individual boxes are added as the student progresses through the tasks. A task panel on the left hand side allows the user to select a task, upon which a popup window will slide open on the right where they enter content. This content is then displayed on the workspace in the background in a box (which can be moved around to organise, seen in frame 3 ). Additional icons on left and right lead to new tasks.
Updates
The wireframe mockup of the application has been updated - please ignore the previous one, which has now been deleted. This is the final version to work from.
Reason: Would like to give more time to allow for a design that meets the young children target audience and for more creative ways for icons and colour schemes.
Reason: We are waiting for some further submissions to come through.
Target Market(s)
9-12 year old school children, so the design should be appealing to both boys and girls.
Industry/Entity Type
Graphic Design
Look and feel
Each slider illustrates characteristics of the customer's brand and the style your logo design should communicate.

```html
<!DOCTYPE html>
<html lang="en">
<head>
<meta charset="utf-8">
<title>Brivolen – Essay Writing</title>
<link href="https://fonts.googleapis.com/css2?family=Ubuntu:ital,wght@0,300;0,400;0,500;1,300;1,400;1,500&display=swap" rel="stylesheet">
<style>
  :root {
    --lime-top: #cdec7a;
    --lime-bar: #86c72c;
    --lime-bar-dark: #5fa51a;
    --lime-bg: #9ad43a;
    --lime-light: #d8f3a0;
    --orange: #f9a92c;
    --orange-tabs: #fcc22a;
    --tab-circle: #f8a222;
    --menu-text: #3b2a12;
    --magenta: #a3195b;
    --magenta-light: #d9679b;
    --popup-text: #6d5a4c;
    --panel-white: #ffffff;
    --panel-grey: #e4e4e4;
    --icon-dark: #4a4a4a;
    --logo: #8cb92a;
  }
  * { box-sizing: border-box; margin: 0; padding: 0; }
  html, body { width: 1200px; height: 900px; overflow: hidden; background: #f4f6f8; }
  body { font-family: "Ubuntu", sans-serif; }

  .app {
    position: relative; width: 1200px; height: 900px; overflow: hidden;
    background:
      radial-gradient(circle at 1050px 700px, rgba(255,255,240,.95) 0, rgba(240,252,200,.6) 140px, transparent 330px),
      radial-gradient(circle at 900px 420px, rgba(255,255,255,.35) 0, transparent 120px),
      radial-gradient(circle at 60px 820px, rgba(255,255,255,.25) 0, transparent 110px),
      linear-gradient(160deg, var(--lime-bg) 0%, #a7dc4a 45%, var(--lime-light) 100%);
  }

  /* Top toolbar */
  .toolbar {
    position: absolute; left: 0; top: 0; width: 1200px; height: 96px;
    background: linear-gradient(to bottom, var(--lime-top) 0%, #a6d94e 45%, var(--lime-bar) 75%, var(--lime-bar-dark) 100%);
  }
  .copyright {
    position: absolute; top: 3px; width: 100%; text-align: center;
    font-size: 14px; font-style: italic; color: #4d5a2a;
  }
  .nav-btn {
    position: absolute; top: 22px; width: 50px; height: 50px; border-radius: 50%;
    background: radial-gradient(circle at 50% 35%, #c6e972, #86c430 70%, #6aa91f);
    box-shadow: inset 0 1px 2px rgba(255,255,255,.6), 0 1px 2px rgba(0,0,0,.2);
    display: flex; align-items: center; justify-content: center;
  }
  .nav-btn svg { width: 18px; height: 18px; fill: #5c7a28; }
  .address-field {
    position: absolute; left: 342px; top: 29px; width: 520px; height: 35px;
    border-radius: 5px; background: #fff; border: 1px solid #9cbf5e;
  }
  .search-field {
    position: absolute; left: 993px; top: 29px; width: 172px; height: 35px;
    border-radius: 5px; background: #fff; border: 1px solid #9cbf5e;
  }
  .search-field .search-btn {
    position: absolute; right: 0; top: 0; width: 34px; height: 33px;
    border-left: 1px solid #ccc; display: flex; align-items: center; justify-content: center;
  }

  /* Left icon column */
  .side-tool { position: absolute; width: 90px; text-align: center; font-size: 15px; font-style: italic; color: #4a5a2e; }
  .side-tool svg { display: block; margin: 0 auto 4px; }

  /* Task panel */
  .task-panel {
    position: absolute; left: 110px; top: 106px; width: 250px; height: 794px;
    background: var(--orange);
  }
  .level-tabs {
    height: 94px; background: var(--orange-tabs);
    display: flex; justify-content: space-around; padding: 10px 8px 0;
    border-bottom: 2px solid #f3d25a;
  }
  .level-tab { text-align: center; font-size: 12px; font-style: italic; color: #4a3410; width: 72px; }
  .level-tab .badge {
    width: 48px; height: 48px; border-radius: 50%; margin: 0 auto 6px;
    background: radial-gradient(circle at 50% 40%, #fbb23a, var(--tab-circle) 70%, #ea8f14);
    display: flex; align-items: center; justify-content: center;
    font-size: 12px; font-weight: 500; color: #5a3a0f;
  }
  .task-menu { list-style: none; padding-top: 46px; }
  .task-menu li { height: 48.5px; padding-left: 18px; font-size: 21px; font-weight: 300; color: var(--menu-text); }
  .task-menu li.sub { padding-left: 33px; }

  /* Popup */
  .popup {
    position: absolute; left: 371px; top: 108px; width: 382px; height: 784px;
    border: 2px solid var(--magenta); border-radius: 10px; overflow: hidden;
    background: linear-gradient(to bottom, var(--panel-white) 0%, var(--panel-white) 60%, var(--panel-grey) 100%);
  }
  .popup-header {
    position: relative; height: 62px;
    background: linear-gradient(to bottom, var(--magenta-light) 0%, #bb3472 45%, var(--magenta) 100%);
  }
  .popup-title {
    position: absolute; left: 24px; top: 17px; color: #fff;
    font-size: 21px; font-style: italic; font-weight: 500;
  }
  .popup-close {
    position: absolute; right: 12px; top: 7px; width: 48px; height: 48px; border-radius: 50%;
    background: linear-gradient(to bottom, #e586b0, #b02a69); border: 2px solid #f3b8d2;
    display: flex; align-items: center; justify-content: center;
  }
  .popup-text {
    position: absolute; left: 26px; top: 70px; width: 340px;
    font-size: 19.5px; line-height: 25.4px; font-style: italic; font-weight: 300; color: var(--popup-text);
  }
  .question-input {
    position: absolute; left: 24px; top: 490px; width: 336px; height: 188px;
    border: 1px solid #b9b9b9; border-radius: 6px; background: #fff;
    padding: 10px 12px; font-size: 19.5px; line-height: 25px; font-style: italic; font-weight: 300; color: #7a6a5c;
  }
  .enter-btn {
    position: absolute; left: 252px; top: 696px; width: 104px; height: 34px; border-radius: 17px;
    border: 1px solid #b5b5b5; background: linear-gradient(to bottom, #fff, #dcdcdc);
    font-size: 19px; font-style: italic; color: #6d6d6d; text-align: center; line-height: 32px;
  }

  /* Right tools */
  .tool { position: absolute; left: 1088px; width: 90px; text-align: center; font-size: 15px; font-style: italic; color: #4e5e38; }
  .tool svg { display: block; margin: 0 auto 2px; }

  .brand-name {
    position: absolute; right: 16px; bottom: 14px; font-size: 32px; line-height: 1; font-weight: 400;
    letter-spacing: 0; color: var(--logo); white-space: nowrap;
  }
</style>
</head>
<body>
<main class="app">
  <header class="toolbar">
    <p class="copyright">Brivolen.com.au © 2012</p>
    <div class="nav-btn" style="left:32px"><svg viewBox="0 0 10 10"><path d="M7 1 L2 5 L7 9 Z"/></svg></div>
    <div class="nav-btn" style="left:101px"><svg viewBox="0 0 10 10"><path d="M3 1 L8 5 L3 9 Z"/></svg></div>
    <div class="nav-btn" style="left:171px"><svg viewBox="0 0 10 10"><path d="M2 2 L8 8 M8 2 L2 8" stroke="#5c7a28" stroke-width="2" fill="none"/></svg></div>
    <div class="nav-btn" style="left:240px"><svg viewBox="0 0 10 10"><path d="M5 1 L0.5 5 H2 V9 H4 V6.5 H6 V9 H8 V5 H9.5 Z"/></svg></div>
    <div class="address-field"></div>
    <div class="search-field">
      <div class="search-btn">
        <svg width="16" height="16" viewBox="0 0 16 16"><circle cx="6.5" cy="6.5" r="4.5" fill="none" stroke="#666" stroke-width="2"/><path d="M10 10 L14 14" stroke="#666" stroke-width="2"/></svg>
      </div>
    </div>
  </header>

  <div class="side-tool" style="left:0;top:122px">
    <svg width="40" height="34" viewBox="0 0 40 34"><path d="M6 6 C18 4 30 12 34 28 C26 20 16 14 6 6 Z" fill="#3f4a35"/><path d="M6 6 L30 26" stroke="#a8d25a" stroke-width="1"/></svg>
    Lesson
  </div>
  <div class="side-tool" style="left:0;top:200px">
    <svg width="40" height="38" viewBox="0 0 40 38"><rect x="4" y="4" width="32" height="26" rx="2" fill="#f3f3f3" stroke="#555" stroke-width="2"/><rect x="4" y="4" width="32" height="6" fill="#777"/><path d="M28 22 L36 30 L32 30 L34 35 L32 36 L30 31 L27 33 Z" fill="#222"/></svg>
    Activities
  </div>

  <nav class="task-panel">
    <div class="level-tabs">
      <div class="level-tab"><div class="badge">B</div>Newbie</div>
      <div class="level-tab"><div class="badge"><svg width="14" height="14" viewBox="0 0 10 10"><path d="M8 1 L2 5 L8 9 Z" fill="#5a3a0f"/></svg></div>Developer</div>
      <div class="level-tab"><div class="badge"><svg width="20" height="20" viewBox="0 0 20 20"><g stroke="#5a3a0f" stroke-width="2"><path d="M10 1 V19 M1 10 H19 M3.5 3.5 L16.5 16.5 M16.5 3.5 L3.5 16.5"/></g><circle cx="10" cy="10" r="4" fill="#5a3a0f"/></svg></div>Star</div>
    </div>
    <ul class="task-menu">
      <li>ESSAY WRITING</li>
      <li>Overview</li>
      <li>The Question</li>
      <li class="sub">Teacher-Set Q</li>
      <li class="sub">You own Q</li>
      <li class="sub">Pick a Q</li>
      <li>Decoding the Q</li>
      <li>You Ideas</li>
      <li>Structure</li>
      <li>Writing</li>
      <li>Review</li>
    </ul>
  </nav>

  <section class="popup">
    <div class="popup-header">
      <h2 class="popup-title">Teacher-Set Question</h2>
      <div class="popup-close"><svg width="14" height="14" viewBox="0 0 10 10"><path d="M2 2 L8 8 M8 2 L2 8" stroke="#fff" stroke-width="2.2"/></svg></div>
    </div>
    <p class="popup-text">If you teacher has given<br>you a question or topic<br>for this essay, then can enter<br>below. Then we can<br>work on decoding it<br>into th specific key words<br>than you will need to<br>recognise from the question<br>that will allow you to answer it<br>in the best way.<br>If you don´t understand<br>any words in the<br>question, use the<br>Dictionary (in the Reference<br>section to the right) to<br>check for the meaning of the word.</p>
    <div class="question-input">Enter the question your<br>teacher has given here...</div>
    <div class="enter-btn">Enter</div>
  </section>

  <div class="tool" style="top:130px">
    <svg width="34" height="40" viewBox="0 0 34 40"><circle cx="17" cy="12" r="9" fill="#555"/><path d="M2 40 C2 26 32 26 32 40 Z" fill="#555"/></svg>
    My Name
  </div>
  <div class="tool" style="top:210px">
    <svg width="34" height="36" viewBox="0 0 34 36"><rect x="3" y="18" width="6" height="16" fill="#555"/><rect x="12" y="12" width="6" height="22" fill="#555"/><rect x="21" y="6" width="6" height="28" fill="#555"/><path d="M2 12 L14 6 L22 8 L32 2" stroke="#555" stroke-width="2" fill="none"/></svg>
    Reference
  </div>
  <div class="tool" style="top:290px">
    <svg width="42" height="32" viewBox="0 0 42 32"><rect x="2" y="4" width="38" height="24" fill="none" stroke="#555" stroke-width="3"/><rect x="11" y="9" width="20" height="14" fill="#555"/><g fill="#555"><rect x="3" y="8" width="4" height="3"/><rect x="3" y="21" width="4" height="3"/><rect x="35" y="8" width="4" height="3"/><rect x="35" y="21" width="4" height="3"/></g></svg>
    Samples
  </div>
  <div class="tool" style="top:372px">
    <svg width="38" height="36" viewBox="0 0 38 36"><rect x="3" y="3" width="28" height="30" rx="3" fill="#555"/><rect x="9" y="3" width="16" height="10" fill="#ddd"/><rect x="8" y="19" width="18" height="12" fill="#ddd"/><path d="M30 14 V26 M25 19 L30 14 L35 19" stroke="#555" stroke-width="3" fill="none"/></svg>
    Save
  </div>
  <div class="tool" style="top:458px">
    <svg width="38" height="38" viewBox="0 0 38 38"><path d="M6 32 L26 12" stroke="#555" stroke-width="5"/><circle cx="28" cy="10" r="7" fill="none" stroke="#555" stroke-width="4"/><path d="M6 6 L32 32" stroke="#555" stroke-width="4"/></svg>
    Settings
  </div>
  <div class="tool" style="top:540px">
    <svg width="30" height="36" viewBox="0 0 30 36"><rect x="6" y="3" width="20" height="30" fill="none" stroke="#555" stroke-width="2"/><path d="M6 3 L18 8 V36 L6 33 Z" fill="#555"/><path d="M0 18 H12 M8 14 L12 18 L8 22" stroke="#555" stroke-width="2" fill="none"/></svg>
    Exit
  </div>

  <p class="brand-name">BRIVOLEN</p>
</main>
</body>
</html>
```